Redesign business cards

We have a new logo and I am not that happy with the layout of our existing card and looking for a change. Font is a bit small and the green can be hard to read. Logo may need a tidy up as the copy I have is not that hi-res too so require you to produce a hi-res version of the logo for us too. There will be three individual business cards to produce with just the names and phone numbers being different. Address will change too, but use what you see on the card for now.

Industry/Entity Type

Business

Requirements
Nice to have
• You could consider a redesign to the new logo, just not too radical. We like the blue and green hexagons as we feel that they are representative of oil industry that we are in.

```html
<!DOCTYPE html>
<html lang="en">
<head>
<meta charset="utf-8">
<title>Verdan Oil Services — Business Cards</title>
<link href="https://fonts.googleapis.com/css2?family=Nunito+Sans:wght@400;600;800&display=swap" rel="stylesheet">
<style>
  :root {
    --bg: #e9e9eb;
    --paper: #ffffff;
    --ink: #24323a;
    --ink-soft: #4a5a63;
    --blue: #00a6e6;
    --blue-deep: #0077b6;
    --green: #8cc43f;
    --green-deep: #3f7d1f;
    --tint-blue: #dff1fa;
    --tint-green: #e8f3da;
    --shadow: rgba(0, 0, 0, 0.12);
  }
  * { box-sizing: border-box; margin: 0; padding: 0; }
  html, body { width: 1200px; height: 861px; overflow: hidden; }
  body {
    background: var(--bg);
    font-family: "Nunito Sans", Arial, sans-serif;
    color: var(--ink);
  }
  .card-sheet {
    width: 1200px;
    height: 861px;
    display: grid;
    grid-template-columns: 460px 460px;
    grid-template-rows: 281px 281px;
    gap: 44px 48px;
    justify-content: center;
    align-content: center;
  }
  .card {
    position: relative;
    width: 460px;
    height: 281px;
    border-radius: 3px;
    overflow: hidden;
    box-shadow: 0 6px 18px var(--shadow);
  }

  /* Edition colours: deep tones carry text on white, bright tones fill the backs */
  .card--green { --band: var(--green-deep); --accent-text: var(--green-deep); --mark: var(--blue); --tint: var(--tint-green); --fill: var(--green); }
  .card--blue  { --band: var(--blue-deep);  --accent-text: var(--blue-deep);  --mark: var(--green); --tint: var(--tint-blue);  --fill: var(--blue); }

  /* Front */
  .card--front { background: var(--paper); }
  .name-band {
    position: absolute;
    left: 0; top: 0;
    width: 300px; height: 64px;
    background: var(--band);
    color: #fff;
    padding: 12px 0 0 26px;
  }
  .name-band__name { font-size: 19px; font-weight: 800; line-height: 24px; }
  .name-band__creds { font-size: 10px; font-weight: 600; margin-left: 6px; opacity: 0.9; }
  .name-band__role { font-size: 12px; font-weight: 400; line-height: 16px; }

  .contact-list {
    position: absolute;
    left: 26px; top: 82px;
    list-style: none;
    font-size: 13px;
    line-height: 20px;
    font-weight: 600;
    color: var(--ink);
  }
  .texture-area {
    position: absolute;
    left: 14px; top: 156px;
    width: 170px; height: 100px;
    background: radial-gradient(ellipse at 45% 50%, var(--tint) 0%, rgba(255,255,255,0) 70%);
  }
  .wordmark {
    position: absolute;
    display: flex;
    align-items: center;
    gap: 10px;
  }
  .wordmark__text { font-weight: 800; line-height: 1; }
  .wordmark__mark { display: block; }

  .card--front .wordmark { left: 232px; top: 138px; }
  .card--front .wordmark__text { font-size: 30px; color: var(--accent-text); }
  .card--front .wordmark__mark { width: 18px; height: 18px; background: var(--mark); }

  .address {
    position: absolute;
    left: 234px; top: 180px;
    font-style: normal;
    font-size: 13px;
    line-height: 19px;
    color: var(--ink-soft);
  }
  .address__company { font-weight: 800; color: var(--ink); }

  /* Back */
  .card--back { background: var(--fill); }
  .card--back .wordmark { left: 50%; top: 50%; transform: translate(-50%, -50%); }
  .card--back .wordmark__text { font-size: 40px; color: #fff; }
  .card--back .wordmark__mark { width: 24px; height: 24px; background: #fff; }
</style>
</head>
<body>
<main class="card-sheet">

  <section class="card card--front card--green" aria-label="Business card front, green edition">
    <header class="name-band">
      <div class="name-band__name">Corin Walsh<span class="name-band__creds">BEng (Mech) RPEQ</span></div>
      <div class="name-band__role">Director</div>
    </header>
    <ul class="contact-list">
      <li>+61 400 555 018</li>
      <li>corin@verdanoil.co.nz</li>
      <li>www.verdanoil.com.au</li>
    </ul>
    <div class="texture-area" role="img" aria-label="Faint hexagon texture"></div>
    <div class="wordmark">
      <span class="wordmark__text">Verdan</span>
      <span class="wordmark__mark"></span>
    </div>
    <address class="address">
      <span class="address__company">Verdan Oil Services</span><br>
      412 Harbour Road<br>
      PO Box 5170<br>
      Eastbrook QLD 4170
    </address>
  </section>

  <section class="card card--back card--green" aria-label="Business card back, green edition">
    <div class="wordmark">
      <span class="wordmark__text">Verdan</span>
      <span class="wordmark__mark"></span>
    </div>
  </section>

  <section class="card card--front card--blue" aria-label="Business card front, blue edition">
    <header class="name-band">
      <div class="name-band__name">Corin Walsh<span class="name-band__creds">BEng (Mech) RPEQ</span></div>
      <div class="name-band__role">Director</div>
    </header>
    <ul class="contact-list">
      <li>+61 400 555 018</li>
      <li>corin@verdanoil.co.nz</li>
      <li>www.verdanoil.com.au</li>
    </ul>
    <div class="texture-area" role="img" aria-label="Faint hexagon texture"></div>
    <div class="wordmark">
      <span class="wordmark__text">Verdan</span>
      <span class="wordmark__mark"></span>
    </div>
    <address class="address">
      <span class="address__company">Verdan Oil Services</span><br>
      412 Harbour Road<br>
      PO Box 5170<br>
      Eastbrook QLD 4170
    </address>
  </section>

  <section class="card card--back card--blue" aria-label="Business card back, blue edition">
    <div class="wordmark">
      <span class="wordmark__text">Verdan</span>
      <span class="wordmark__mark"></span>
    </div>
  </section>

</main>
</body>
</html>
```